Puslishing House Needs poster Design for Medical Book

We need an advertisement desing for a medical book on cardiology named "Vertentes" (Hypertension), which 2nd Edition we launched last August. What makes this book special is that this is the first time in history that a hypertension book has a second edition in Brazil and was written by the Vascular Unit of the Southern Clinical Guild of Heart Studies in comemoration in its 100 years. The two news about this book is that we sold 1000 units since we launched (which is good) and we have now an ebook version for all tablet, smartphones and readers. From this month on it is going to happen importants hypertension meetings and we want to promote this two news about this book - 1000 units sold and ebook version. We would like to see designs that use orange (the publishing house color) and communicate celebration.

Target Market(s)

Doctors Specialist from several segments like Cardiology, Endocrinology, Nephrology, Nutrition. Most of the target are man with 50 years-old.

Industry/Entity Type

Medical

Requirements
Must have
• The adverstisement must have the attached book cover and publishing house logo (Marlowan) using only the name (without the tree) or the complete logo.
Should not have
• The design should not use old-style, serif fonts like Times new Roman.

```html
<!DOCTYPE html>
<html lang="pt">
<head>
<meta charset="utf-8">
<title>Vertentes – 1000 obras vendidas</title>
<link rel="stylesheet" href="https://fonts.googleapis.com/css2?family=Quicksand:wght@300;400;700&family=Oswald:wght@500;700&family=Roboto+Condensed:wght@700&display=swap">
<style>
  :root{
    --orange-light:#f9a13a;
    --orange:#f47b20;
    --orange-deep:#ec6a1c;
    --orange-panel:#f28a1e;
    --white:#ffffff;
    --cover-green:#1f5a45;
    --cover-green-mid:#5f8f7c;
    --cover-title:#e8503a;
    --cover-ink:#1d2a2a;
    --gold-dark:#b98a3e;
    --gold-light:#f3dca0;
    --device-dark:#1b1b1b;
  }
  *{margin:0;padding:0;box-sizing:border-box}
  html,body{width:847px;height:1200px;overflow:hidden;background:var(--orange)}
  .poster{
    position:relative;width:847px;height:1200px;overflow:hidden;
    background:radial-gradient(ellipse at 50% 45%,var(--orange-light) 0%,var(--orange) 55%,var(--orange-deep) 100%);
    font-family:"Quicksand",sans-serif;color:var(--white);
  }
  .ribbon-bow{
    position:absolute;right:0;top:0;width:275px;height:243px;
    background:linear-gradient(135deg,var(--gold-light),var(--gold-dark));
    clip-path:polygon(30% 0,100% 0,100% 100%,80% 70%,45% 55%,10% 40%,35% 25%);
    opacity:.9;
  }
  .headline{position:absolute;left:0;right:0;top:150px;text-align:center;line-height:1}
  .headline__count{display:block;font-weight:300;font-size:80px;letter-spacing:1px}
  .headline__sold{display:block;font-weight:700;font-size:82px;margin-top:4px}
  .headline__ebook{display:block;font-weight:300;font-size:52px;margin-top:6px}
  .book-cover{
    position:absolute;left:212px;top:377px;width:426px;height:572px;
    background:linear-gradient(180deg,var(--cover-green) 0%,var(--cover-green-mid) 28%,#eef2f0 48%,#ffffff 60%);
    box-shadow:0 6px 18px rgba(0,0,0,.25);overflow:hidden;
  }
  .book-cover__authors{
    position:absolute;left:240px;top:70px;font-family:"Roboto Condensed",sans-serif;
    font-weight:700;font-size:19px;line-height:30px;color:var(--white);
  }
  .book-cover__title{
    position:absolute;left:0;right:0;top:200px;text-align:center;
    font-family:"Oswald",sans-serif;font-weight:700;font-size:76px;letter-spacing:1px;color:var(--cover-title);
  }
  .book-cover__photo{
    position:absolute;left:0;right:0;top:300px;height:180px;
    background:radial-gradient(ellipse at 60% 50%,#9aa5a8 0%,#d7dcdc 45%,#ffffff 80%);
  }
  .book-cover__footer{position:absolute;left:0;right:0;bottom:0;height:90px}
  .publisher-tag{
    position:absolute;left:22px;top:18px;width:50px;height:56px;border:1px solid #555;
    display:flex;align-items:flex-end;justify-content:center;padding-bottom:3px;
    font-size:8px;font-weight:700;color:var(--cover-ink);
  }
  .book-cover__edition{position:absolute;left:92px;top:52px;font-family:"Roboto Condensed",sans-serif;font-size:15px;color:var(--cover-ink)}
  .partner-badge{position:absolute;left:240px;top:42px;width:30px;height:30px;border-radius:50%;background:#3b6fb0}
  .department-tag{
    position:absolute;left:284px;top:40px;width:130px;
    font-family:"Roboto Condensed",sans-serif;font-weight:700;font-size:8px;line-height:10px;color:#b5232a;
    text-transform:uppercase;
  }
  .publisher-block{
    position:absolute;left:30px;top:1022px;width:110px;height:120px;background:var(--white);
    display:flex;align-items:flex-end;justify-content:center;padding-bottom:10px;
    font-weight:700;font-size:17px;color:var(--orange-deep);
  }
  .availability{
    position:absolute;left:140px;top:1022px;width:371px;height:120px;background:var(--orange-panel);
    padding:18px 14px;font-size:27px;line-height:29px;font-weight:300;
  }
  .availability strong{font-weight:700;font-size:23px}
  .devices{
    position:absolute;left:523px;top:1010px;width:286px;height:152px;
    background:linear-gradient(180deg,#2a2a2a 0%,var(--device-dark) 60%,#bfbfbf 100%);
    border-radius:6px;
  }
  .gold-band{
    position:absolute;left:0;right:0;bottom:0;height:23px;
    background:linear-gradient(90deg,var(--gold-dark),var(--gold-light) 50%,var(--gold-dark));
  }
</style>
</head>
<body>
<main class="poster">
  <div class="ribbon-bow" role="img" aria-label="Golden gift ribbon and bow across the corner"></div>

  <h1 class="headline">
    <span class="headline__count">1000 obra</span>
    <span class="headline__sold">vendidos</span>
    <span class="headline__ebook">e versão em e-book</span>
  </h1>

  <section class="book-cover" aria-label="Vertentes book cover">
    <div class="book-cover__authors">Lívia R. Montenegro<br>Caio Ferraz<br>Otávio Lemes</div>
    <div class="book-cover__title">VERTENTES</div>
    <div class="book-cover__photo" role="img" aria-label="Photograph of a blood pressure gauge and bulb"></div>
    <div class="book-cover__footer">
      <div class="publisher-tag">Marlowan</div>
      <div class="book-cover__edition">2º EDIÇÃO</div>
      <div class="partner-badge"></div>
      <div class="department-tag">Vascular Unit of the Southern Clinical Guild of Heart Studies</div>
    </div>
  </section>

  <div class="publisher-block">Marlowan</div>
  <div class="availability">This applications<br>is available in<br><strong>SMARTPHONES &amp; TABLET PC</strong></div>
  <div class="devices" role="img" aria-label="Desktop, tablet and smartphone showing the e-book"></div>

  <div class="gold-band"></div>
</main>
</body>
</html>
```